Brisk Hive 360 Postcard Design, Double-Sided

Please read carefully and see attached. Designers that do not follow these instructions will not be selected. Limit ONE design submission per artist. The ONE design submission shall show both the front and the back designs. Designs must comply with the attached dismensions accounting for the bleed area to prevent designs from being cut off during printing. The attached business card and door tag designs have already been created, printed and are in use. The postcard shall be similar in design to the attached business card and door tag. All of the information that you need is attached. The overall size is 4.12" x 6.12" for the front. The back is different, see attached and scale to match template. I would like the Veteran Owned Business logo added as well. It would also be nice to see my photo incorporated somehow. I like the yellow on the door tag. It helps build contrast and pops out. Again, one design submission per designer that shows both the front and the back.

Target Market(s)

Please read all instructions and see attached.

Industry/Entity Type

Requirements
Must have
• Please read all instructions and see attached.
Nice to have
Should not have

```html
<!DOCTYPE html>
<html lang="en">
<head>
<meta charset="utf-8">
<title>Brisk Hive 360 Postcard</title>
<link href="https://fonts.googleapis.com/css2?family=Poppins:wght@400;500;700&family=Arimo:wght@400;700&display=swap" rel="stylesheet">
<style>
  :root {
    --backdrop: #c3c3c3;
    --ink: #111111;
    --black: #0b0b0b;
    --white: #ffffff;
    --yellow: #ffef00;
    --alert-red: #e60000;
    --soft-grey: #efefef;
    --rule-grey: #d9d9d9;
    --badge-navy: #1d2f6b;
  }
  html, body {
    margin: 0;
    width: 1200px;
    height: 1200px;
    overflow: hidden;
    background: var(--backdrop);
  }
  .postcard {
    position: absolute;
    left: 252px;
    width: 696px;
    height: 467px;
    background: var(--white);
    box-shadow: 0 3px 6px rgba(0,0,0,0.25);
    overflow: hidden;
    font-family: "Poppins", sans-serif;
    color: var(--ink);
  }
  .postcard--front { top: 138px; }
  .postcard--back { top: 644px; }
  .postcard svg.shape-layer { position: absolute; left: 0; top: 0; }

  .brand-mark {
    position: absolute;
    display: flex;
    align-items: center;
    gap: 8px;
    font-family: "Poppins", sans-serif;
    font-weight: 700;
    color: var(--white);
    white-space: nowrap;
  }
  .brand-mark .brand-dot {
    border: 3px solid var(--white);
    border-radius: 50%;
  }
  .brand-mark--front { left: 175px; top: 119px; font-size: 26px; transform: translate(-50%, -50%); }
  .brand-mark--front .brand-dot { width: 18px; height: 18px; }
  .brand-mark--back { left: 16px; top: 76px; font-size: 16px; gap: 6px; z-index: 2; }
  .brand-mark--back .brand-dot { width: 11px; height: 11px; border-width: 2px; }

  .services {
    position: absolute;
    left: 423px;
    top: 12px;
    color: var(--white);
  }
  .services-title {
    margin: 0;
    font-weight: 700;
    font-size: 24px;
    line-height: 28px;
    color: var(--yellow);
  }
  .services-list {
    margin: 2px 0 0;
    padding: 0 0 0 28px;
    font-size: 18px;
    font-weight: 500;
    line-height: 23px;
  }

  .house-art {
    position: absolute;
    left: 181px;
    top: 282px;
    width: 320px;
    height: 175px;
    border-radius: 160px 160px 0 0;
    background: linear-gradient(180deg, rgba(230,230,230,0.5), var(--soft-grey));
  }
  .owner {
    position: absolute;
    left: 35px;
    top: 288px;
  }
  .owner-name {
    margin: 0;
    font-weight: 700;
    font-size: 29px;
    line-height: 36px;
    letter-spacing: -0.3px;
  }
  .owner-role {
    margin: 0;
    font-weight: 400;
    font-size: 20px;
    line-height: 24px;
  }
  .owner-perks {
    margin: 8px 0 0;
    padding-left: 21px;
    font-size: 13px;
    line-height: 17px;
  }
  .divider {
    position: absolute;
    left: 345px;
    top: 302px;
    width: 1px;
    height: 101px;
    background: var(--ink);
  }
  .contacts {
    position: absolute;
    left: 384px;
    top: 288px;
    margin: 0;
    padding: 0;
    list-style: none;
    font-size: 19px;
    white-space: nowrap;
  }
  .contacts li {
    display: flex;
    align-items: center;
    gap: 6px;
    height: 35px;
  }
  .contacts svg { flex: none; }
  .text-tag { color: var(--alert-red); font-weight: 700; margin-left: 6px; }
  .bottom-rule {
    position: absolute;
    left: 9px;
    right: 8px;
    top: 457px;
    height: 1px;
    background: var(--rule-grey);
  }

  .owner-photo {
    position: absolute;
    left: 172px;
    top: 30px;
    width: 212px;
    height: 340px;
    border-radius: 100px 100px 0 0;
    background: linear-gradient(180deg, #c9ccd1 0%, #b9bdc4 55%, rgba(255,255,255,0) 100%);
  }
  .postage-box {
    position: absolute;
    left: 567px;
    top: 9px;
    width: 117px;
    height: 116px;
    border: 1px solid #555;
    display: flex;
    align-items: center;
    justify-content: center;
    font-family: "Arimo", sans-serif;
    font-weight: 700;
    font-size: 12px;
    letter-spacing: 0.3px;
  }
  .mail-address {
    position: absolute;
    left: 427px;
    top: 264px;
    margin: 0;
    font-family: "Arimo", sans-serif;
    font-style: normal;
    font-size: 16px;
    line-height: 23px;
  }
  .veteran-badge {
    position: absolute;
    left: 32px;
    top: 356px;
    width: 86px;
    height: 86px;
    border-radius: 50%;
    background: var(--badge-navy);
  }
</style>
</head>
<body>

<section class="postcard postcard--front">
  <svg class="shape-layer" width="696" height="467" viewBox="0 0 696 467" aria-hidden="true">
    <path d="M0,0 H696 V258 C620,242 520,232 400,244 C240,262 100,262 0,230 Z" fill="var(--yellow)"/>
    <path d="M0,0 H696 V246 C620,232 520,224 400,234 C240,250 100,246 0,222 Z" fill="var(--black)"/>
  </svg>

  <div class="brand-mark brand-mark--front"><span class="brand-dot"></span>Brisk Hive 360</div>

  <div class="services">
    <h2 class="services-title">SERVICES:</h2>
    <ul class="services-list">
      <li>Assembly</li>
      <li>Small Repairs</li>
      <li>Wifi / Router Setup</li>
      <li>Fabrication</li>
      <li>Hanging Items</li>
      <li>Wireless Device Setup</li>
      <li>Odd Jobs</li>
    </ul>
  </div>

  <div class="house-art" role="img" aria-label="Faint illustration of a house surrounded by tools"></div>

  <div class="owner">
    <h1 class="owner-name">DANA R. WHITLOCK</h1>
    <p class="owner-role">OWNER &amp; HANDYMAN</p>
    <ul class="owner-perks">
      <li>Fast Response</li>
      <li>High Quality</li>
      <li>Fair Pricing</li>
      <li>Veteran Owned</li>
    </ul>
  </div>

  <div class="divider"></div>

  <ul class="contacts">
    <li>
      <svg width="24" height="24" viewBox="0 0 24 24" aria-hidden="true"><circle cx="12" cy="12" r="11" fill="var(--ink)"/><path d="M12 5a4.5 4.5 0 0 0-4.5 4.5c0 3.3 4.5 8.5 4.5 8.5s4.5-5.2 4.5-8.5A4.5 4.5 0 0 0 12 5z" fill="var(--white)"/><circle cx="12" cy="9.5" r="1.6" fill="var(--ink)"/></svg>
      Bayport, Florida
    </li>
    <li>
      <svg width="24" height="24" viewBox="0 0 24 24" aria-hidden="true"><circle cx="12" cy="12" r="11" fill="var(--ink)"/><rect x="6" y="8" width="12" height="8" rx="1" fill="var(--white)"/><path d="M6 8.5 12 13l6-4.5" fill="none" stroke="var(--ink)" stroke-width="1.3"/></svg>
      Service@BriskHive360.com
    </li>
    <li>
      <svg width="24" height="24" viewBox="0 0 24 24" aria-hidden="true"><circle cx="12" cy="12" r="11" fill="var(--ink)"/><path d="M8.5 6.5l2 2.6-1.2 1.4c.8 1.7 2.1 3 3.8 3.8l1.4-1.2 2.6 2-1.1 2c-4.6-.4-8.3-4.1-8.7-8.7z" fill="var(--white)"/></svg>
      (555) 014-2236<span class="text-tag">TEXT</span>
    </li>
    <li>
      <svg width="24" height="24" viewBox="0 0 24 24" aria-hidden="true"><g fill="none" stroke="var(--ink)" stroke-width="1.6"><circle cx="12" cy="12" r="9.5"/><ellipse cx="12" cy="12" rx="4.2" ry="9.5"/><path d="M2.5 12h19M4 7h16M4 17h16"/></g></svg>
      BriskHive360.com
    </li>
  </ul>

  <div class="bottom-rule"></div>
</section>

<section class="postcard postcard--back">
  <svg class="shape-layer" width="696" height="467" viewBox="0 0 696 467" aria-hidden="true">
    <path d="M0,0 H538 C520,72 482,112 398,130 C300,152 205,162 128,214 C65,256 22,300 0,356 Z" fill="var(--yellow)"/>
    <path d="M0,0 H528 C505,60 470,95 390,118 C300,142 200,150 120,200 C60,238 20,270 0,309 Z" fill="var(--black)"/>
  </svg>

  <div class="brand-mark brand-mark--back"><span class="brand-dot"></span>Brisk Hive 360</div>

  <div class="owner-photo" role="img" aria-label="Portrait photo of the owner in a grey polo shirt"></div>

  <div class="postage-box">POSTAGE</div>

  <address class="mail-address">
    John Smith<br>
    123 Main Street<br>
    Small Town, USA 00000-0000
  </address>

  <div class="veteran-badge" role="img" aria-label="Veteran owned business membership badge"></div>
</section>

</body>
</html>
```